Business Card Design

We just need these details on one side of card and logo on the other.

Industry/Entity Type

Business

Contact Information for Business Card

Colette Marsh | Artist
87 Tillbrook Lane
Dunmore Heights Vic 3172
# 0418 207 913 | 03 9386 2417
colette@colettemarsh-example.com
colettesstudio-example.com.au

```html
<!DOCTYPE html>
<html lang="en">
<head>
<meta charset="utf-8">
<title>Colette's Studio – Business Card</title>
<link rel="stylesheet" href="https://fonts.googleapis.com/css2?family=Lato:wght@400;700&display=swap">
<style>
  :root {
    --page-bg: #d9d9d9;
    --card-bg: #262626;
    --card-edge: #1c1c1c;
    --lime: #a6c83a;
    --ink-light: #f2f2f2;
    --ink-deep: #121212;
    --card-shadow: rgba(0, 0, 0, 0.28);
  }
  * { margin: 0; padding: 0; box-sizing: border-box; }
  html, body {
    width: 1200px;
    height: 926px;
    overflow: hidden;
    background: var(--page-bg);
    font-family: "Lato", sans-serif;
  }
  .sheet {
    position: relative;
    width: 1200px;
    height: 926px;
    display: flex;
    align-items: center;
    justify-content: center;
    gap: 44px;
  }
  .card {
    position: relative;
    width: 540px;
    height: 309px;
    background: var(--card-bg);
    border: 1px solid var(--card-edge);
    box-shadow: 0 10px 26px var(--card-shadow);
  }

  /* Front: contact side */
  .card-front { padding: 34px 36px; }
  .brand-name {
    font-family: "Lato", sans-serif;
    font-weight: 400;
    color: var(--ink-light);
    font-size: 30px;
    letter-spacing: 0.5px;
    line-height: 1;
  }
  .person-name {
    margin-top: 44px;
    color: var(--lime);
    font-weight: 400;
    font-size: 19px;
    letter-spacing: 3px;
    text-transform: uppercase;
  }
  .contact-list {
    list-style: none;
    margin-top: 12px;
  }
  .contact-item {
    display: flex;
    align-items: center;
    gap: 10px;
    color: var(--ink-light);
    font-size: 13px;
    letter-spacing: 0.6px;
    line-height: 21px;
  }
  .contact-item.is-strong { font-weight: 700; }
  .contact-icon {
    width: 11px;
    height: 11px;
    flex: none;
    fill: var(--lime);
  }

  /* Back: brand side */
  .card-back {
    display: flex;
    flex-direction: column;
    align-items: center;
    justify-content: center;
  }
  .card-back .brand-name {
    color: var(--ink-deep);
    font-size: 50px;
    text-shadow: none;
  }
  .web-address {
    margin-top: 42px;
    color: var(--lime);
    font-size: 13px;
    letter-spacing: 3px;
  }
</style>
</head>
<body>
<main class="sheet">

  <section class="card card-front" aria-label="Business card, contact side">
    <p class="brand-name">Colette's Studio</p>
    <h1 class="person-name">Colette Marsh</h1>
    <ul class="contact-list">
      <li class="contact-item is-strong">
        <svg class="contact-icon" viewBox="0 0 12 12" aria-hidden="true"><path d="M1 4c0-2 2-3 5-3s5 1 5 3l-2 1-1-1.5H4L3 5zM3 6h6l1 5H2z"/></svg>
        0418 207 913
      </li>
      <li class="contact-item is-strong">
        <svg class="contact-icon" viewBox="0 0 12 12" aria-hidden="true"><path d="M3.5 0h5a1 1 0 0 1 1 1v10a1 1 0 0 1-1 1h-5a1 1 0 0 1-1-1V1a1 1 0 0 1 1-1zm.5 1.5v8h4v-8z"/></svg>
        03 9386 2417
      </li>
      <li class="contact-item">
        <svg class="contact-icon" viewBox="0 0 12 12" aria-hidden="true"><path d="M4.5 8.5l-1 1a1.4 1.4 0 0 1-2-2l2-2a1.4 1.4 0 0 1 2 0l.8-.8a2.5 2.5 0 0 0-3.6 0l-2 2a2.5 2.5 0 0 0 3.6 3.6l1-1zM7.5 3.5l1-1a1.4 1.4 0 0 1 2 2l-2 2a1.4 1.4 0 0 1-2 0l-.8.8a2.5 2.5 0 0 0 3.6 0l2-2A2.5 2.5 0 0 0 7.7.7l-1 1zM4 7.3L7.3 4l.7.7L4.7 8z"/></svg>
        colettesstudio-example.com.au
      </li>
      <li class="contact-item">
        <svg class="contact-icon" viewBox="0 0 12 12" aria-hidden="true"><path d="M0 2h12v1L6 7 0 3zM0 4.2l6 4 6-4V10H0z"/></svg>
        colette@colettemarsh-example.com
      </li>
      <li class="contact-item">
        <svg class="contact-icon" viewBox="0 0 12 12" aria-hidden="true"><path d="M6 0a4 4 0 0 1 4 4c0 3-4 8-4 8S2 7 2 4a4 4 0 0 1 4-4zm0 2.3A1.7 1.7 0 1 0 6 5.7 1.7 1.7 0 0 0 6 2.3z"/></svg>
        Artist 87 Tillbrook Lane Dunmore Heights Vic 3172
      </li>
    </ul>
  </section>

  <section class="card card-back" aria-label="Business card, brand side">
    <p class="brand-name">Colette's Studio</p>
    <p class="web-address">www.colettesstudio-example.com.au</p>
  </section>

</main>
</body>
</html>
```